Dental Medical History Form - Content provided

Design a medical history form for a dental practice. Content is provided so all that is needed is the formatting to make it look great and easy to read.

"Patient Information" to include all information contained in top portion of the "Patient Medical History Form" docx file.

"Medical History" should follow the formatting and content of the "Exact Medical History" file as this is what the entry fields look like in our practice software and so we would like it to match.

1st page - Patient info, allergies, medications, antibiotics, joint replacement, pregnancy.

2nd page - Do you have, or have you had, any of the following? . . . . . . .
Updates

Project Deadline Extended Reason: Picked too short of a deadline to start (2 days) Added Monday, February 13, 2017

Target Market(s)

All ages but must be clear enough for elderly to read. Use as much space as possible to keep font size bigger yet keep to two pages

Industry/Entity Type

Dental

Font styles to use
Sans Serif

Requirements
Must have
• All content provided
• Our logo at the top (file provided)
• Century Gothic Font
• Limit to two pages

```html
<!DOCTYPE html>
<html lang="en">
<head>
<meta charset="utf-8">
<title>Confidential Medical History – Harbourline Dental</title>
<link rel="stylesheet" href="https://fonts.googleapis.com/css2?family=Didact+Gothic&family=Montserrat:wght@600;700&display=swap">
<style>
  :root{
    --backdrop:#000;
    --page:#fff;
    --ink:#1b1b1b;
    --rule:#2a2a2a;
    --body:"Didact Gothic", "Century Gothic", sans-serif;
    --head:"Montserrat", "Century Gothic", sans-serif;
  }
  *{box-sizing:border-box;margin:0;padding:0}
  html,body{width:1200px;height:1000px;overflow:hidden;background:var(--backdrop)}
  body{font-family:var(--body);color:var(--ink);position:relative}
  .page{position:absolute;top:100px;height:800px;background:var(--page)}
  .page--front{left:25px;width:566px}
  .page--back{left:610px;width:565px}
  .page > *{position:absolute}

  .practice-name{left:70px;top:40px;width:225px;text-align:right;color:var(--ink);font-family:var(--body);font-size:21px;line-height:24px;white-space:nowrap}
  .practice-address{left:310px;top:31px;width:160px;text-align:center;font-size:11px;line-height:14px;white-space:nowrap}
  .form-title{left:0;width:566px;top:95px;text-align:center;font-family:var(--head);font-weight:700;font-size:15.5px;letter-spacing:.2px}

  .field{display:flex;align-items:flex-end;font-size:11px;line-height:14px;white-space:nowrap}
  .field .rule{flex:1;border-bottom:1px solid var(--rule);margin-left:3px;height:10px}
  .rule-line{height:8px;border-bottom:1px solid var(--rule)}
  .hint{font-size:7.5px;font-style:italic;line-height:9px}
  .label-italic{font-size:11px;font-style:italic;line-height:14px}
  .plain{font-size:11px;line-height:14px;white-space:nowrap}

  .section-title{font-family:var(--head);font-weight:600;font-size:11.5px;line-height:15px;white-space:nowrap}
  .choice{display:flex;align-items:center;font-size:11px;line-height:14px;white-space:nowrap}
  .box{display:inline-block;width:11px;height:11px;border:1px solid var(--rule);margin-right:6px;flex:none}
  .entry{border:1px solid var(--rule);height:17px}
  .turnover{font-family:var(--head);font-weight:700;font-size:8.5px;line-height:12px;text-align:right;width:46px}

  .checklist{list-style:none;width:280px}
  .checklist li{display:flex;align-items:center;font-size:10px;white-space:nowrap}
  .checklist--left li{height:16.87px}
  .checklist--right li{height:16.7px}
  .checklist .box{width:11px;height:11px;margin-right:9px}
  .checklist .group{font-family:var(--head);font-weight:600;font-size:10.5px}
  .thanks{left:0;width:565px;text-align:center;font-size:9.5px;font-style:italic;line-height:13px}
</style>
</head>
<body>

<section class="page page--front">
  <div class="practice-name">Harbourline Dental</div>
  <div class="practice-address">Suite 4/118 Ridgeway Rd<br>Corrin NSW 2261<br>(02) 40 555 018</div>
  <h1 class="form-title">CONFIDENTIAL MEDICAL HISTORY</h1>

  <div class="field" style="left:21px;top:134px;width:247px">Name:<span class="rule"></span></div>
  <span class="hint" style="left:73px;top:148px">Title</span>
  <span class="hint" style="left:111px;top:148px">First</span>
  <span class="hint" style="left:154px;top:148px">Middle</span>
  <span class="hint" style="left:218px;top:148px">Last</span>
  <div class="field" style="left:21px;top:170px;width:247px">Address:<span class="rule"></span></div>
  <div class="field" style="left:21px;top:194px;width:247px">DOB:<span class="rule"></span></div>
  <div class="field" style="left:21px;top:219px;width:247px">Email Address:<span class="rule"></span></div>
  <div class="field" style="left:21px;top:243px;width:247px">Phone Number(s):<span class="rule"></span></div>
  <div class="rule-line" style="left:21px;top:264px;width:247px"></div>
  <span class="hint" style="left:83px;top:273px">Mobile</span>
  <span class="hint" style="left:136px;top:273px">Work</span>
  <span class="hint" style="left:180px;top:273px">Home</span>
  <div class="label-italic" style="left:21px;top:297px">Emergency Contact Person:</div>
  <div class="field" style="left:21px;top:322px;width:247px">Name:<span class="rule"></span></div>
  <div class="field" style="left:21px;top:346px;width:247px">Relationship:<span class="rule"></span></div>
  <div class="field" style="left:21px;top:371px;width:247px">Phone number:<span class="rule"></span></div>

  <div class="label-italic" style="left:283px;top:134px">General Practitioner:</div>
  <div class="field" style="left:283px;top:159px;width:259px">Name:<span class="rule"></span></div>
  <div class="field" style="left:283px;top:183px;width:262px">Practice Name:<span class="rule"></span></div>
  <div class="field" style="left:283px;top:208px;width:262px">Phone Number:<span class="rule"></span></div>
  <div class="plain" style="left:283px;top:227px">Do you have a health fund with dental cover?</div>
  <div class="choice" style="left:283px;top:243px"><span class="box"></span>Yes</div>
  <div class="choice" style="left:345px;top:243px"><span class="box"></span>No</div>
  <div class="plain" style="left:283px;top:265px">If so, what is the name of the fund?</div>
  <div class="rule-line" style="left:283px;top:285px;width:262px"></div>
  <div class="field" style="left:283px;top:303px;width:262px">Fund Number?<span class="rule"></span></div>
  <div class="plain" style="left:283px;top:322px;word-spacing:6px"><span style="word-spacing:0">Priority Number on card:</span>&nbsp; 0 1 2 3 4 5</div>
  <div class="field" style="left:283px;top:349px;width:262px">Occupation:<span class="rule"></span></div>
  <div class="field" style="left:283px;top:374px;width:262px">Referrred by:<span class="rule"></span></div>

  <h2 class="section-title" style="left:21px;top:408px">Please indicate if&nbsp; you are allergic to any of the following?</h2>
  <div class="choice" style="left:23px;top:437px"><span class="box"></span>Aspirin</div>
  <div class="choice" style="left:98px;top:437px"><span class="box"></span>Codeine</div>
  <div class="choice" style="left:186px;top:437px"><span class="box"></span>Penicillin</div>
  <div class="choice" style="left:273px;top:437px"><span class="box"></span>Sulfites</div>
  <div class="choice" style="left:350px;top:437px"><span class="box"></span>Latex</div>
  <div class="choice" style="left:23px;top:456px"><span class="box"></span>Local Anaesthetic</div>
  <div class="choice" style="left:162px;top:456px"><span class="box"></span>Lactose</div>
  <div class="choice" style="left:246px;top:456px"><span class="box"></span>Nickel</div>
  <div class="plain" style="left:21px;top:476px">Other:</div>
  <div class="entry" style="left:60px;top:475px;width:338px"></div>

  <h2 class="section-title" style="left:21px;top:504px">Are you currently taking, or have ever taken, any of the following medication?</h2>
  <div class="choice" style="left:23px;top:533px"><span class="box"></span>Asthma inhaler</div>
  <div class="choice" style="left:145px;top:533px"><span class="box"></span>Anti-epileptics</div>
  <div class="choice" style="left:263px;top:533px"><span class="box"></span>Anti-depressants</div>
  <div class="choice" style="left:394px;top:533px"><span class="box"></span>Blood Pressure</div>
  <div class="choice" style="left:23px;top:552px"><span class="box"></span>Blood Thinners</div>
  <div class="choice" style="left:140px;top:552px"><span class="box"></span>Bisphosphonates</div>
  <div class="choice" style="left:273px;top:552px"><span class="box"></span>Chemotherapy</div>
  <div class="choice" style="left:398px;top:552px"><span class="box"></span>Insulin</div>
  <div class="choice" style="left:23px;top:571px"><span class="box"></span>Immunosuppressants</div>
  <div class="choice" style="left:178px;top:571px"><span class="box"></span>Steroids</div>
  <div class="choice" style="left:259px;top:571px"><span class="box"></span>Oral Contraceptive</div>
  <div class="choice" style="left:407px;top:571px"><span class="box"></span>Other</div>

  <h2 class="section-title" style="left:21px;top:599px">Please specify medication name, dose, and frequency where possible:</h2>
  <div class="plain" style="left:21px;top:620px">Notes</div>
  <div class="entry" style="left:57px;top:618px;width:341px"></div>
  <div class="plain" style="left:21px;top:641px">Notes</div>
  <div class="entry" style="left:57px;top:640px;width:341px"></div>

  <div class="plain" style="left:21px;top:682px">Do you require antibiotic cover?</div>
  <div class="choice" style="left:248px;top:682px"><span class="box"></span>Yes</div>
  <div class="choice" style="left:311px;top:682px"><span class="box"></span>No</div>
  <div class="plain" style="left:21px;top:704px">Have you had a joint replacement?</div>
  <div class="choice" style="left:248px;top:704px"><span class="box"></span>Yes</div>
  <div class="choice" style="left:311px;top:704px"><span class="box"></span>No</div>
  <div class="label-italic" style="left:21px;top:726px">Women:</div>
  <div class="plain" style="left:21px;top:742px">Are you pregnant?</div>
  <div class="choice" style="left:250px;top:742px"><span class="box"></span>Yes</div>
  <div class="choice" style="left:311px;top:742px"><span class="box"></span>No</div>
  <div class="choice" style="left:371px;top:742px"><span class="box"></span>Possible</div>
  <div class="plain" style="left:21px;top:764px">Breast Feeding?</div>
  <div class="choice" style="left:250px;top:764px"><span class="box"></span>Yes</div>
  <div class="choice" style="left:311px;top:764px"><span class="box"></span>No</div>

  <div class="turnover" style="left:486px;top:769px">Please turnover</div>
  <svg class="turnover-icon" style="left:536px;top:768px" width="25" height="26" viewBox="0 0 25 26" aria-hidden="true">
    <path d="M1 1 H24 V25 H12 L1 1 Z" fill="none" stroke="#1b1b1b" stroke-width="1.2"/>
    <path d="M12 25 L24 13 L24 25 Z" fill="#1b1b1b"/>
  </svg>
</section>

<section class="page page--back">
  <h2 class="section-title" style="left:21px;top:19px">Do you have, or have you had, any of the following?</h2>

  <ul class="checklist checklist--left" style="left:21px;top:35.5px">
    <li class="group">Dental</li>
    <li><span class="box"></span>Acid Reflux</li>
    <li><span class="box"></span>Bad Breath/TasteBleeding/Swollen/Sore Gums</li>
    <li><span class="box"></span>Blisters/Ulcers in Mouth</li>
    <li><span class="box"></span>Broken tooth/filling</li>
    <li><span class="box"></span>Burning tongue</li>
    <li><span class="box"></span>Dry mouth</li>
    <li><span class="box"></span>Food collection between teeth</li>
    <li><span class="box"></span>Grinding/clenching teeth (day/night)</li>
    <li><span class="box"></span>Loose teeth</li>
    <li><span class="box"></span>Crooked teeth</li>
    <li><span class="box"></span>Discoloured teeth</li>
    <li><span class="box"></span>Sensitivity to Hot/Cold</li>
    <li><span class="box"></span>Tooth pain when chewing</li>
    <li><span class="box"></span>Jaw pain/Fracture</li>
    <li><span class="box"></span>Orthodontic treatment/history</li>
    <li><span class="box"></span>Oral Cancer</li>
    <li class="group">Diet/Lifestyle</li>
    <li><span class="box"></span>Drink more than one glass alcohol per day</li>
    <li><span class="box"></span>Smoking</li>
    <li><span class="box"></span>Carbonated drinks</li>
    <li><span class="box"></span>Sugary foods</li>
    <li class="group">Blood</li>
    <li><span class="box"></span>Anaemia</li>
    <li><span class="box"></span>Blood clots</li>
    <li><span class="box"></span>Leukemia</li>
    <li><span class="box"></span>Low platelets</li>
    <li><span class="box"></span>Lymphoma</li>
    <li><span class="box"></span>Haemophelia</li>
    <li class="group">Chest</li>
    <li><span class="box"></span>Bronchitis</li>
    <li><span class="box"></span>Cystic Fibrosis</li>
    <li><span class="box"></span>Emphysema</li>
    <li><span class="box"></span>Pneumonia</li>
    <li class="group">Infectious Disease</li>
    <li><span class="box"></span>Creutzfeldt-Jakob Disease</li>
    <li><span class="box"></span>Hepatitis A,B,C,D</li>
    <li><span class="box"></span>HIV/AIDS</li>
    <li><span class="box"></span>Influenza</li>
  </ul>

  <ul class="checklist checklist--right" style="left:321px;top:37.6px;width:230px">
    <li><span class="box"></span>Shingles</li>
    <li><span class="box"></span>Tuberculosis</li>
    <li class="group">Heart</li>
    <li><span class="box"></span>Angina</li>
    <li><span class="box"></span>Atrial Fibrillation</li>
    <li><span class="box"></span>Blood Pressure (High/Low)</li>
    <li><span class="box"></span>Congenital Heart Disease</li>
    <li><span class="box"></span>Heart attack</li>
    <li><span class="box"></span>Heart murmur</li>
    <li><span class="box"></span>Heart surgery</li>
    <li><span class="box"></span>Heart valve replacement</li>
    <li><span class="box"></span>Infective endocarditis</li>
    <li><span class="box"></span>Rheumatic Heart Disease</li>
    <li><span class="box"></span>Pacemaker</li>
    <li><span class="box"></span>Stent</li>
    <li class="group">Other</li>
    <li><span class="box"></span>Anxiety/PTSD</li>
    <li><span class="box"></span>Arthritis</li>
    <li><span class="box"></span>Alzheimer’s</li>
    <li><span class="box"></span>Asthma</li>
    <li><span class="box"></span>Anaphylaxis</li>
    <li><span class="box"></span>Auto-immune disease</li>
    <li><span class="box"></span>Coeliac</li>
    <li><span class="box"></span>Depression</li>
    <li><span class="box"></span>Diabetes</li>
    <li><span class="box"></span>Epilepsy</li>
    <li><span class="box"></span>Kidney Disease</li>
    <li><span class="box"></span>Liver Disease</li>
    <li><span class="box"></span>Osteoporosis</li>
    <li><span class="box"></span>Parkinson’s</li>
    <li><span class="box"></span>Radiation to Head/Neck</li>
    <li><span class="box"></span>Schizophrenia</li>
    <li><span class="box"></span>Sring</li>
    <li><span class="box"></span>Sleep apnea</li>
    <li><span class="box"></span>Stroke</li>
  </ul>

  <div class="plain" style="left:322px;top:627px;font-size:10px">Other:</div>
  <div class="entry" style="left:322px;top:642px;width:221px;height:16px"></div>
  <div class="entry" style="left:322px;top:660px;width:221px;height:16px"></div>
  <div class="entry" style="left:322px;top:677px;width:221px;height:16px"></div>

  <div class="field" style="left:21px;top:712px;width:277px;font-size:10px">Signature:<span class="rule"></span></div>
  <div class="field" style="left:317px;top:712px;width:228px;font-size:10px">Date:<span class="rule"></span></div>

  <p class="thanks" style="top:738px">Thank you for the time to complete your medical history form.</p>
  <p class="thanks" style="top:756px">Oral health is linked to overall health and this comprehensive questionnaire<br>will help us to provide you with optimal and safe care.</p>
</section>

</body>
</html>
```